Handyman Business Card and website logo design

I need a logo for my new handyman business. The logo will be used for my website, business cards, and Facebook pages. I want my business card to have this logo and have a simplistic and nicely flowing design with a handyman feel.

The name of my business is KT Nest Fixer. (Dr is for doctor NOT Drive). So my thoughts for my logo is a handyman with a stethoscope and looking like a doctor examining a house. With handyman will have a tool-belt on and holding a drill or some other well recognized tool. Basically a handyman doctor examining someones "precious home" so that he can prescribe the right "fix" for them.

Contact Information for Business Card

Martin Pellow (CEO)
KTNestFixer
4170 Willowmere Court
Naperville, IL 60571

```html
<!DOCTYPE html>
<html lang="en">
<head>
<meta charset="utf-8">
<title>KT Nest Fixer – Business Card</title>
<link rel="stylesheet" href="https://fonts.googleapis.com/css2?family=Barlow:wght@400;700&display=swap">
<style>
  :root {
    --page-bg: #ffffff;
    --brown-dark: #6b5435;
    --gold: #af884a;
    --tan-light: #d4b893;
    --tan-mid: #a88c63;
    --text-light: #ffffff;
  }
  * { margin: 0; padding: 0; box-sizing: border-box; }
  html, body {
    width: 1200px;
    height: 1000px;
    overflow: hidden;
    background: var(--page-bg);
    font-family: "Barlow", sans-serif;
  }
  .business-card {
    position: absolute;
    left: 346px;
    top: 55px;
    width: 506px;
    height: 890px;
    background: var(--gold);
    color: var(--text-light);
  }
  .card-header {
    position: absolute;
    left: 0;
    top: 0;
    width: 100%;
    height: 470px;
    background: var(--brown-dark);
  }
  .house-illustration {
    position: absolute;
    left: 42px;
    top: 35px;
    width: 442px;
    height: 262px;
    border-radius: 24px;
    background: linear-gradient(135deg, var(--tan-light) 0%, var(--tan-mid) 100%);
    opacity: 0.85;
  }
  .brand-name {
    position: absolute;
    left: 74px;
    top: 302px;
    font-weight: 700;
    font-size: 74px;
    line-height: 62px;
    letter-spacing: 1px;
    text-transform: uppercase;
  }
  .contact-block {
    position: absolute;
    left: 74px;
    top: 515px;
    font-weight: 400;
    font-size: 25px;
    line-height: 35px;
  }
  .contact-name {
    font-weight: 700;
    font-size: 23px;
    margin-bottom: 10px;
  }
  .contact-role { font-size: 17px; letter-spacing: 0.5px; }
  .contact-address { margin-bottom: 11px; }
  .contact-line { margin-bottom: 14px; }
</style>
</head>
<body>
  <article class="business-card">
    <header class="card-header">
      <div class="house-illustration" role="img" aria-label="Illustration of a house with a stethoscope looped around it"></div>
      <h1 class="brand-name">KT Nest<br>Fixer</h1>
    </header>
    <section class="contact-block">
      <p class="contact-name">Martin Pellow <span class="contact-role">(CEO)</span></p>
      <p class="contact-address">KT Nest Fixer<br>4170 Willowmere Court<br>Naperville, IL 60571</p>
      <p class="contact-line">Call: (123) 345-6789</p>
      <p class="contact-line">Email: mp@ktnestfixer.com</p>
      <p class="contact-line">Web: www.ktnestfixer.com</p>
    </section>
    <footer class="card-footer" style="position:absolute;left:0;bottom:0;width:100%;height:40px;background:var(--brown-dark);"></footer>
  </article>
</body>
</html>
```